Tending the Hidden Garden; A Map Toward Calm, Purpose & Belonging

I need a book cover, for the above book title. This is a journey of the heart to know the heart of God. I think on the text, Simple (see below graphic)
Black Lettering for Tending.....Garden
Gold lettering for God
Either gold or black for the subtitle; A Map Toward Calm, Purpose, & Belonging
I would like the below graphic idea only no photograph of a person,
and White background instead of black
Simple Font, like below graphic, but open to suggestions

not age specific, Every person has been given a heart to know God, we are taking the mystery out the process to understand God is Father, loving gracious, ever present, etc. If we know His heart, we realize He's not at a distance, He is there, an ever present help

Security

• Title: Tending the Hidden Garden; A Map Toward Calm, Purpose, & Belonging
• My name, Rob Fenwick
• See Below Graphic

```html
<!DOCTYPE html>
<html lang="en">
<head>
<meta charset="utf-8">
<title>Tending the Hidden Garden — Rob Fenwick</title>
<link href="https://fonts.googleapis.com/css2?family=Anton&family=EB+Garamond:wght@500&family=Libre+Baskerville:wght@700&display=swap" rel="stylesheet">
<style>
  :root {
    --paper: #ffffff;
    --sky-soft: #eef1f7;
    --sky-cloud: #c9d1e4;
    --sky-deep: #9aa7c8;
    --ink: #161616;
    --gold-light: #e2b955;
    --gold-mid: #c4912c;
    --gold-dark: #8d6216;
    --subtitle: #7a5512;
    --author: #2a2418;
    --shadow: rgba(40, 36, 30, 0.35);
  }
  html, body {
    margin: 0;
    padding: 0;
    overflow: hidden;
    background: var(--paper);
  }
  .cover {
    position: relative;
    width: 801px;
    height: 1200px;
    overflow: hidden;
    background: var(--paper);
  }
  .cover__sky {
    position: absolute;
    left: 0;
    right: 0;
    top: 680px;
    bottom: 0;
    background:
      radial-gradient(ellipse 40% 55% at 68% 70%, rgba(255,255,255,0.9), rgba(255,255,255,0) 70%),
      linear-gradient(180deg,
        var(--paper) 0%,
        var(--sky-soft) 25%,
        var(--sky-cloud) 65%,
        var(--sky-deep) 100%);
  }
  .cover__title {
    position: absolute;
    left: 0;
    top: 0;
    width: 801px;
    height: 600px;
  }
  .cover__title text {
    font-family: "Anton", "Impact", sans-serif;
    text-anchor: middle;
  }
  .cover__subtitle {
    position: absolute;
    left: 0;
    right: 0;
    top: 626px;
    margin: 0;
    text-align: center;
    font-family: "EB Garamond", Georgia, serif;
    font-weight: 500;
    font-size: 35px;
    line-height: 44px;
    color: var(--subtitle);
  }
  .cover__author {
    position: absolute;
    left: 0;
    right: 0;
    top: 1080px;
    margin: 0;
    text-align: center;
    font-family: "Libre Baskerville", Georgia, serif;
    font-weight: 700;
    font-size: 56px;
    line-height: 70px;
    color: var(--author);
  }
</style>
</head>
<body>
  <main class="cover">
    <div class="cover__sky" role="img" aria-label="Soft pale clouds with light breaking through and a raised open hand reaching upward"></div>

    <svg class="cover__title" viewBox="0 0 801 600" aria-labelledby="book-title">
      <title id="book-title">Tending the Hidden Garden</title>
      <defs>
        <linearGradient id="grad-gold" x1="0" y1="0" x2="0" y2="1">
          <stop offset="0" stop-color="var(--gold-light)"/>
          <stop offset="0.55" stop-color="var(--gold-mid)"/>
          <stop offset="1" stop-color="var(--gold-dark)"/>
        </linearGradient>
        <filter id="title-shadow" x="-10%" y="-10%" width="120%" height="130%">
          <feDropShadow dx="3" dy="4" stdDeviation="3" flood-color="#2a2418" flood-opacity="0.35"/>
        </filter>
      </defs>
      <g filter="url(#title-shadow)">
        <text x="394" y="212" font-size="182" textLength="548" lengthAdjust="spacingAndGlyphs" fill="var(--ink)">TENDING</text>
        <text x="400" y="392" font-size="182" textLength="580" lengthAdjust="spacingAndGlyphs" fill="url(#grad-gold)">THE HIDDEN</text>
        <text x="392" y="564" font-size="168" textLength="600" lengthAdjust="spacingAndGlyphs" fill="var(--ink)">GARDEN</text>
      </g>
    </svg>

    <p class="cover__subtitle">A Map Toward Calm, Purpose &amp; Belonging</p>
    <p class="cover__author">Rob Fenwick</p>
  </main>
</body>
</html>
```